Business card for Real Estate Company located in Coastal area of spain

Want a business card design. Simple, professional, horizontal layout. will be 2 sided. Name of company (logo big on front). Name of agent, phone and email address. Back side will be list of general services we provide. Would like to see 2 separate concepts using the 2 separate logo treatments. One using Rich dark, bright blue as the stock color, and the other using White as the stock color.
Logo files uploaded (2 different versions) Domain (harbourkeyestates.com) Moraira-Calpe-Altea-Javea-Denia-Marina Alta Area (perhaps across the bottom of the front of card0 Ingrid Tavel Licensed Estate Agent / Partner Ingrid@harbourkeyestates.com +34.611.48.27.09 Back of card should list services offered

Real Estate Sales and Investments Real Estate Rental Management Kitchen, Bathroom Reformations Complete Home Reformation Services Window and Door Replacement Landscape and Garden Management Pool and Jacuzzi Service

Target Market(s)

Real estate and construction

Industry/Entity Type

Real Estate

Contact Information for Business Card

Logo files uploaded (2 different versions) Domain (harbourkeyestates.com) Moraira-Calpe-Altea-Javea-Denia-Marina Alta Area (perhaps across the bottom of the front of card0 Ingrid Tavel Licensed Estate Agent / Partner Ingrid@harbourkeyestates.com +34.611.48.27.09

Colors

Designer to choose colors to be used in the design.

Requirements
Must have
• progressive look professional
Nice to have
• Front big logo, Agent details. Back, list of services included in project description
Should not have
• Gloss finish for card

```html
<!DOCTYPE html>
<html lang="en">
<head>
<meta charset="utf-8">
<title>Harbourkeyestates.com – Business Card</title>
<link rel="stylesheet" href="https://fonts.googleapis.com/css2?family=Open+Sans:wght@400;500;700&family=Montserrat:wght@400;500&family=Oswald:wght@500&display=swap">
<style>
  :root {
    --page-bg: #e4e4e6;
    --card-bg: #f1f1f3;
    --brand-blue: #173c8e;
    --brand-violet: #5a45b4;
    --ink-grey: #4a4a4e;
    --name-grey: #56565a;
    --swoosh-white: #f6f6f8;
  }
  * { box-sizing: border-box; margin: 0; padding: 0; }
  html, body { width: 1200px; height: 831px; overflow: hidden; }
  body { background: var(--page-bg); position: relative; font-family: "Montserrat", sans-serif; }

  .card {
    position: absolute; left: 288px; width: 624px; height: 357px;
    background: var(--card-bg); border-radius: 18px; overflow: hidden;
    box-shadow: 0 2px 6px rgba(0,0,0,0.12);
  }
  .card--front { top: 42px; }
  .card--back { top: 432px; }
  .card__art { position: absolute; inset: 0; width: 624px; height: 357px; }

  .company-name {
    position: absolute; left: 52px; top: 28px; width: 520px; text-align: center;
    font-family: "Open Sans", sans-serif; font-weight: 500; font-size: 41px;
    color: var(--brand-blue); line-height: 1;
  }

  .agent { position: absolute; left: 38px; top: 150px; }
  .agent__name { font-family: "Open Sans", sans-serif; font-size: 40px; line-height: 1; letter-spacing: -0.5px; }
  .agent__first { font-weight: 700; color: var(--brand-blue); }
  .agent__last { font-weight: 400; color: var(--name-grey); }
  .agent__title {
    margin-top: 14px; font-family: "Oswald", sans-serif; font-weight: 500;
    font-size: 12.5px; letter-spacing: 2.2px; color: var(--ink-grey);
  }
  .agent__rule { width: 66px; height: 2px; background: var(--brand-blue); margin-top: 10px; }

  .contact { position: absolute; left: 36px; top: 257px; list-style: none; }
  .contact__item { display: flex; align-items: center; height: 27px; font-size: 11.5px; color: var(--ink-grey); }
  .contact__icon { width: 24px; height: 26px; margin-right: 12px; }

  .services { position: absolute; left: 24px; top: 62px; }
  .services__title {
    font-family: "Open Sans", sans-serif; font-weight: 700; font-size: 29px;
    color: var(--brand-blue); line-height: 1;
  }
  .services__list { list-style: none; margin-top: 12px; }
  .services__item {
    display: flex; align-items: center; font-size: 19px; line-height: 22.3px; color: var(--ink-grey);
  }
  .services__item::before {
    content: ""; width: 8px; height: 8px; background: var(--brand-blue);
    margin-right: 18px; flex: none;
  }

  .company-name--small {
    left: 20px; top: 322px; width: auto; text-align: left; font-size: 12.5px;
  }
</style>
</head>
<body>

<svg width="0" height="0" style="position:absolute" aria-hidden="true">
  <defs>
    <linearGradient id="cornerGradient" x1="0" y1="1" x2="1" y2="0">
      <stop offset="0" stop-color="#173c8e"/>
      <stop offset="1" stop-color="#5a45b4"/>
    </linearGradient>
    <linearGradient id="photoGradient" x1="0.3" y1="0" x2="0.5" y2="1">
      <stop offset="0" stop-color="#a6aee6"/>
      <stop offset="0.45" stop-color="#8c8fc4"/>
      <stop offset="0.7" stop-color="#465391"/>
      <stop offset="0.88" stop-color="#8a7a6a"/>
      <stop offset="1" stop-color="#6e7390"/>
    </linearGradient>
  </defs>
</svg>

<!-- Front -->
<section class="card card--front">
  <svg class="card__art" viewBox="0 0 624 357">
    <path d="M0,58 C14,28 40,6 78,0 L0,0 Z" fill="url(#cornerGradient)"/>
    <path role="img" aria-label="Photo of a family house with a lit porch at dusk" d="M624,22 C585,150 470,250 160,357 L624,357 Z" fill="url(#photoGradient)"/>
    <path d="M446,230 C380,280 300,322 212,357 L228,357 C312,323 392,284 446,230 Z" fill="var(--swoosh-white)"/>
  </svg>

  <div class="company-name">Harbourkeyestates.com</div>

  <div class="agent">
    <div class="agent__name"><span class="agent__first">INGRID</span> <span class="agent__last">TAVEL</span></div>
    <div class="agent__title">LICENSED ESTATE AGENT / PARTNER</div>
    <div class="agent__rule"></div>
  </div>

  <ul class="contact">
    <li class="contact__item">
      <svg class="contact__icon" viewBox="0 0 24 26" aria-hidden="true">
        <polygon points="12,1 23,7 23,19 12,25 1,19 1,7" fill="var(--brand-blue)"/>
        <rect x="6.5" y="9" width="11" height="8" fill="none" stroke="#fff" stroke-width="1.2"/>
        <polyline points="6.5,9 12,13.5 17.5,9" fill="none" stroke="#fff" stroke-width="1.2"/>
      </svg>
      Ingrid@harbourkeyestates.com
    </li>
    <li class="contact__item">
      <svg class="contact__icon" viewBox="0 0 24 26" aria-hidden="true">
        <polygon points="12,1 23,7 23,19 12,25 1,19 1,7" fill="var(--brand-blue)"/>
        <path d="M8,8.5 L10,8 L11.2,10.8 L10,11.8 C10.6,13.2 11.8,14.4 13.2,15 L14.2,13.8 L17,15 L16.5,17 C12,17.4 7.6,13 8,8.5 Z" fill="#fff"/>
      </svg>
      +34.611.48.27.09
    </li>
  </ul>
</section>

<!-- Back -->
<section class="card card--back">
  <svg class="card__art" viewBox="0 0 624 357">
    <path d="M0,64 C14,32 40,8 82,0 L0,0 Z" fill="url(#cornerGradient)"/>
    <path role="img" aria-label="Photo of a family house with a lit porch at dusk" d="M624,26 C585,152 470,252 165,357 L624,357 Z" fill="url(#photoGradient)"/>
    <path d="M450,233 C384,282 304,323 216,357 L232,357 C316,324 396,286 450,233 Z" fill="var(--swoosh-white)"/>
  </svg>

  <div class="services">
    <h2 class="services__title">Services Offered</h2>
    <ul class="services__list">
      <li class="services__item">Real Estate Sales and Investments</li>
      <li class="services__item">Real Estate Rental Management</li>
      <li class="services__item">Kitchen, Bathroom Reformations</li>
      <li class="services__item">Complete Home Reformation Services</li>
      <li class="services__item">Window and Door Replacement</li>
      <li class="services__item">Landscape and Garden Management</li>
      <li class="services__item">Pool and Jacuzzi Service</li>
    </ul>
  </div>

  <div class="company-name company-name--small">Harbourkeyestates.com</div>
</section>

</body>
</html>
```